Chiropractic healthcare group business card

We are a Portland Oregon based chiropractic healthcare group. Looking for a new business card design. Something cutting edge, that shows off our new logo and tag line.Use either of the attached logos.Our tag line = "How far could you go pain-free?"I'm open to about anything, impress me!!
Target Market(s)
Chiropractic patients - Auto injury, back pain, sports injuries, neck , shoulder, hip, knee, ankle pain.
Industry/Entity Type
Chiropractic
Contact Information for Business Card
Dr. Bram Tovelund, D.C.
Clinic name - Cedar Chiropractic
2 clinics
location #1
20418 NW Harlow Road
Suite D
Maple Crossing, OR 97481
Location #2
13529 SE Marston Street
Brookhaven OR 97562
Main phone line 971.386.4217
website : www.BirchValeCare.com
Tag line "How far could you go pain-free?"
Colors
Designer to choose colors to be used in the design.
Requirements
Must have
- Use the logo colors -- Want the orange color to be a TRUE orange.
- Both clinic address
- phone number
- website
- personal email - b.tovelund@FreshStrideHealth.com
- tag line - "How far could you go pain-free?"

```html
<!DOCTYPE html>
<html lang="en">
<head>
<meta charset="utf-8">
<title>Cedar Chiropractic – Business Card</title>
<link rel="stylesheet" href="https://fonts.googleapis.com/css2?family=Montserrat:wght@600&family=Open+Sans:wght@600&family=Roboto+Condensed:wght@300;400;500&display=swap">
<style>
  :root {
    --orange: #e89a42;
    --grey: #5a5a5a;
    --white: #ffffff;
    --edge: #cfcfcf;
  }
  html, body {
    margin: 0;
    padding: 0;
    width: 1167px;
    height: 1200px;
    overflow: hidden;
    background: var(--white);
  }
  .card {
    position: absolute;
    left: 149px;
    width: 869px;
    height: 484px;
    box-sizing: border-box;
    overflow: hidden;
  }
  .card--front { top: 81px; background: var(--orange); }
  .card--back { top: 617px; background: var(--white); border: 1px solid var(--edge); }

  .brand-name {
    position: absolute;
    margin: 0;
    font-family: "Montserrat", sans-serif;
    font-weight: 600;
    color: var(--grey);
    white-space: nowrap;
    transform: translate(-50%, -50%);
    letter-spacing: 0.12em;
    text-transform: uppercase;
  }
  .card--front .brand-name { left: 434px; top: 217px; font-size: 40px; }
  .card--back .brand-name { left: 203px; top: 128px; font-size: 24px; }

  .tagline {
    position: absolute;
    left: 0; right: 0;
    top: 420px;
    margin: 0;
    text-align: center;
    font-family: "Open Sans", sans-serif;
    font-weight: 600;
    font-size: 24px;
    letter-spacing: 0.12em;
    color: var(--white);
    line-height: 24px;
  }
  .accent-bar { position: absolute; display: block; }
  .accent-bar--front-left { left: 0; top: 425px; }
  .accent-bar--front-right { right: 0; top: 425px; }
  .accent-bar--name { right: 0; top: 112px; }
  .accent-bar--base { right: 0; bottom: 0; }

  .doctor-name {
    position: absolute;
    left: 480px;
    top: 100px;
    margin: 0;
    font-family: "Roboto Condensed", sans-serif;
    font-weight: 500;
    font-size: 28px;
    color: var(--orange);
    letter-spacing: 0.02em;
    line-height: 32px;
  }
  .contact {
    position: absolute;
    margin: 0;
    font-family: "Roboto Condensed", sans-serif;
    font-weight: 300;
    font-size: 23px;
    line-height: 30px;
    color: var(--grey);
    font-style: normal;
    white-space: nowrap;
  }
  .contact .icon { position: absolute; left: -22px; top: 4px; }
  .contact--clinic-one { left: 90px; top: 262px; }
  .contact--clinic-two { left: 90px; top: 381px; }
  .contact--email { left: 470px; top: 260px; }
  .contact--phone { left: 470px; top: 316px; font-size: 25px; }
  .contact--email .icon { left: -28px; top: 6px; }
  .contact--phone .icon { left: -32px; top: 6px; }
  .website {
    position: absolute;
    left: 466px;
    top: 424px;
    margin: 0;
    font-family: "Roboto Condensed", sans-serif;
    font-weight: 500;
    font-size: 28px;
    color: var(--orange);
    letter-spacing: 0.03em;
    line-height: 32px;
  }
</style>
</head>
<body>

<section class="card card--front" aria-label="Card front">
  <p class="brand-name">Cedar Chiropractic</p>
  <svg class="accent-bar accent-bar--front-left" width="110" height="14" viewBox="0 0 110 14" aria-hidden="true">
    <polygon points="0,0 110,0 102,14 0,14" fill="var(--white)"/>
  </svg>
  <p class="tagline">HOW FAR COULD YOU GO PAIN-FREE?</p>
  <svg class="accent-bar accent-bar--front-right" width="110" height="14" viewBox="0 0 110 14" aria-hidden="true">
    <polygon points="0,0 110,0 110,14 8,14" fill="var(--white)"/>
  </svg>
</section>

<section class="card card--back" aria-label="Card back">
  <p class="brand-name">Cedar Chiropractic</p>

  <h1 class="doctor-name">Dr. Bram Tovelund, D.C.</h1>
  <svg class="accent-bar accent-bar--name" width="87" height="14" viewBox="0 0 87 14" aria-hidden="true">
    <polygon points="0,0 87,0 87,14 7,14" fill="var(--orange)"/>
  </svg>

  <address class="contact contact--clinic-one">
    <svg class="icon" width="14" height="22" viewBox="0 0 14 22" aria-hidden="true">
      <path d="M7 0C3 0 0 3 0 7c0 5 7 15 7 15s7-10 7-15c0-4-3-7-7-7z" fill="var(--orange)"/>
      <circle cx="7" cy="7" r="2.6" fill="var(--white)"/>
    </svg>
    20418 NW Harlow Road<br>Suite D<br>Maple Crossing, OR 97481
  </address>

  <address class="contact contact--clinic-two">
    <svg class="icon" width="14" height="22" viewBox="0 0 14 22" aria-hidden="true">
      <path d="M7 0C3 0 0 3 0 7c0 5 7 15 7 15s7-10 7-15c0-4-3-7-7-7z" fill="var(--orange)"/>
      <circle cx="7" cy="7" r="2.6" fill="var(--white)"/>
    </svg>
    13529 SE Marston Street<br>Brookhaven OR 97562
  </address>

  <p class="contact contact--email">
    <svg class="icon" width="22" height="18" viewBox="0 0 22 18" aria-hidden="true">
      <path d="M1 7 L11 1 L21 7 V17 H1 Z" fill="none" stroke="var(--orange)" stroke-width="1.6" stroke-linejoin="round"/>
      <path d="M1 7 L11 13 L21 7" fill="none" stroke="var(--orange)" stroke-width="1.6"/>
      <circle cx="11" cy="6.5" r="2.6" fill="none" stroke="var(--orange)" stroke-width="1.3"/>
    </svg>
    b.tovelund@FreshStrideHealth.com
  </p>

  <p class="contact contact--phone">
    <svg class="icon" width="20" height="20" viewBox="0 0 20 20" aria-hidden="true">
      <path d="M4 1l3 4-2 3c1 3 4 6 7 7l3-2 4 3-2 3C10 20 0 10 1 3z" fill="var(--orange)"/>
    </svg>
    (971)386-4217
  </p>

  <p class="website">www.BirchValeCare.com</p>
  <svg class="accent-bar accent-bar--base" width="447" height="15" viewBox="0 0 447 15" aria-hidden="true">
    <polygon points="0,0 447,0 447,15 9,15" fill="var(--orange)"/>
  </svg>
</section>

</body>
</html>
```